Logo & Visitenkarte für Buchhaltung und Personal-Management
Zielgruppe
Buchhaltung und Personal- Management für KMUs
Aufgabenstellung
Schrift: Raleway sans-serif (gleich wie Text auf Homepage)
Aktuelle Logo's angefügt müssen aber überarbeitet werden.
Text für Visitenkarte:
Name: Beatrix Vonlanthen
Titel: Fachfrau für Finanz- und Rechnungswesen mit eidg. Fachausweis
Strasse: Kornacker 17
PLZ/Ort: 6318 Talbach
Telefon: 041 675 42 09
Mail: beatrix.vonlanthen@zahlenhort-beispiel.ch
Homepage: www.zahlenhort-beispiel.ch

```html
<!DOCTYPE html>
<html lang="de">
<head>
<meta charset="utf-8">
<title>Visitenkarte zahlenhort-beispiel.ch</title>
<link rel="stylesheet" href="https://fonts.googleapis.com/css2?family=Raleway:wght@400;500;700&display=swap">
<style>
  :root {
    --page: #ffffff;
    --card-front: #f6f4f5;
    --card-back: #dedfd7;
    --band: #f9f7f8;
    --accent: #d6b480;
    --brand-green: #97a795;
    --name-mark: #8fa48a;
    --ink: #1d1d1d;
    --line: #d9d9d9;
  }
  * { box-sizing: border-box; margin: 0; padding: 0; }
  html, body {
    width: 1200px; height: 1200px; overflow: hidden;
    background: var(--page);
    font-family: "Raleway", sans-serif;
    color: var(--ink);
  }
  .card {
    position: absolute;
    left: 285px; width: 630px; height: 408px;
    border: 1px solid var(--line);
    overflow: hidden;
  }
  .card--front { top: 125px; background: var(--card-front); }
  .card--back { top: 668px; background: var(--card-back); }

  .brand {
    position: absolute; left: 64px; top: 159px;
    display: flex; align-items: center; gap: 12px;
  }
  .brand__square {
    width: 88px; height: 88px; border-radius: 10px;
    background: var(--brand-green);
  }
  .brand__name {
    font-weight: 700; font-size: 38px; letter-spacing: 0.5px;
    color: var(--brand-green);
  }

  .person { position: absolute; left: 34px; top: 40px; isolation: isolate; }
  .person__name {
    position: relative; display: inline-block;
    font-size: 24px; font-weight: 500; line-height: 1;
  }
  .person__name::after {
    content: ""; position: absolute; left: 0; right: 0; bottom: -4px; height: 5px;
    border-radius: 3px; background: var(--name-mark); opacity: 0.55; filter: blur(1.5px);
    z-index: -1;
  }
  .person__title {
    margin-top: 14px; font-size: 19.5px; line-height: 24px;
  }
  .address {
    position: absolute; left: 34px; top: 172px; font-size: 19.5px; white-space: pre;
  }

  .contact {
    position: absolute; left: 0; width: 423px; height: 42px;
    background: var(--band);
    display: flex; align-items: center;
    font-size: 19px;
  }
  .contact--phone { top: 227px; }
  .contact--mail { top: 282px; font-size: 16px; }
  .contact--web { top: 337px; }
  .contact__icon {
    position: absolute; left: 9px; top: -5px;
    width: 52px; height: 52px; border-radius: 50%;
    background: var(--accent); color: #fff;
    display: flex; align-items: center; justify-content: center;
    font-family: "Raleway", sans-serif;
    font-weight: 700;
  }
  .contact__icon--at { font-size: 28px; font-weight: 500; }
  .contact__icon--www { font-size: 13px; letter-spacing: 0.5px; padding-top: 4px; }
  .contact__text { margin-left: 77px; white-space: nowrap; }
</style>
</head>
<body>
  <section class="card card--front">
    <div class="brand">
      <div class="brand__square"></div>
      <span class="brand__name">zahlenhort-beispiel.ch</span>
    </div>
  </section>

  <section class="card card--back">
    <div class="person">
      <h1 class="person__name">Beatrix Vonlanthen</h1>
      <p class="person__title">Fachfrau für Finanz- und Rechnungswesen<br>mit eidg. Fachausweis</p>
    </div>
    <p class="address">Kornacker 17   |   6318 Talbach   |   CH</p>

    <div class="contact contact--phone">
      <span class="contact__icon">
        <svg width="18" height="30" viewBox="0 0 18 30" aria-hidden="true">
          <rect x="1.5" y="1.5" width="15" height="27" rx="2.5" fill="none" stroke="#fff" stroke-width="2"/>
          <line x1="2" y1="22" x2="16" y2="22" stroke="#fff" stroke-width="2"/>
          <circle cx="9" cy="25.3" r="1.4" fill="#fff"/>
        </svg>
      </span>
      <span class="contact__text">041 675 42 09</span>
    </div>
    <div class="contact contact--mail">
      <span class="contact__icon contact__icon--at">@</span>
      <span class="contact__text">beatrix.vonlanthen@zahlenhort-beispiel.ch</span>
    </div>
    <div class="contact contact--web">
      <span class="contact__icon contact__icon--www">www</span>
      <span class="contact__text">www.zahlenhort-beispiel.ch</span>
    </div>
  </section>
</body>
</html>
```